Defense Attorney Business Card Design Project/ Stationary

I am looking for a distinctive business card design for my solo law practice.
I practice criminal defense, both juvenile and adult, including DUI. I am a very experienced attorney with prior military experience. The design should convey a traditional, old school flair, but not be too stodgy or uptight. Some color. My logo should appear.

Project Deadline Extended Reason: I misunderstood how this project works and I was not prepared with my logo when this project ran the first time. Added Thursday, November 13, 2014

Reason: I was sent overseas on military duty last year, which interrupted this project. Thank you for your participation... I hope we can get this done this week! Thank you, Ben

Target Market(s)

Regular everyday people looking for strong, knowledgeable, authoritative representation while they are faced with criminal charges. Many have never been charged with a crime before. A reassuring air is therefore desired.

Industry/Entity Type

Business

Contact Information for Business Card

My information is:
Benedict R. Colvin, Attorney at Law
738 Maple Avenue Suite 410
Oakland, California 94607
Tel: (510) 555-0182
Fax: (510) 555-0193
email: bencolvinlaw@quillpost.com
web: www.bencolvinlaw-office.com

Font styles to use
Serif
Sans Serif
Decorative

Colors
0255a3
ffffff

Requirements
Must have
• Sharp lines, bold elements. Conservative use of colors, such as deep blues, burgundy, grays for example.
• While my logo says "Ben Colvin", it should be modified to show "Benedict R. Colvin".
Should not have
• Cliche imagery such as scales of justice, gavels, Tower of Vellandra, etc.

```html
<!DOCTYPE html>
<html lang="en">
<head>
<meta charset="utf-8">
<title>Benedict R. Colvin – Business Card</title>
<link rel="stylesheet" href="https://fonts.googleapis.com/css2?family=Arimo:wght@400&display=swap">
<style>
  :root {
    --navy: #0c3a5a;
    --ink: #1b1b1b;
    --paper: #ffffff;
    --backdrop: #e9e7e3;
  }
  html, body {
    margin: 0;
    padding: 0;
    width: 1200px;
    height: 1000px;
    overflow: hidden;
    background: var(--backdrop);
    font-family: "Arimo", Arial, sans-serif;
  }
  .canvas {
    position: relative;
    width: 1200px;
    height: 1000px;
  }
  .card {
    position: absolute;
    left: 265px;
    width: 667px;
    height: 398px;
    box-sizing: border-box;
    overflow: hidden;
  }
  .card--front {
    top: 73px;
    background: var(--paper);
  }
  .card--back {
    top: 532px;
    background: var(--navy);
  }
  .brand {
    position: absolute;
    display: flex;
    align-items: center;
    gap: 12px;
    font-weight: 400;
    white-space: nowrap;
  }
  .brand__mark {
    display: block;
    flex: none;
  }
  .card--front .brand {
    right: 34px;
    top: 120px;
    font-size: 30px;
    color: var(--navy);
  }
  .card--front .brand__mark {
    width: 18px;
    height: 18px;
    background: var(--navy);
  }
  .card--back .brand {
    left: 0;
    right: 0;
    top: 232px;
    justify-content: center;
    font-size: 42px;
    color: var(--paper);
  }
  .card--back .brand__mark {
    width: 24px;
    height: 24px;
    background: var(--paper);
  }
  .holder {
    position: absolute;
    left: 33px;
    top: 198px;
  }
  .holder__name {
    margin: 0;
    font-size: 20px;
    line-height: 24px;
    color: var(--ink);
    font-weight: 400;
  }
  .holder__title {
    margin: 0;
    font-size: 16px;
    line-height: 20px;
    color: var(--navy);
  }
  .divider {
    position: absolute;
    left: 33px;
    right: 33px;
    top: 250px;
    height: 2px;
    background: var(--navy);
  }
  .contact {
    position: absolute;
    left: 33px;
    top: 265px;
    margin: 0;
    padding: 0;
    list-style: none;
    font-size: 16px;
    line-height: 23.5px;
    color: var(--ink);
  }
  .contact__label {
    color: var(--navy);
  }
  .band {
    position: absolute;
    left: 0;
    right: 0;
    bottom: 0;
    height: 32px;
    background: var(--navy);
  }
</style>
</head>
<body>
<main class="canvas">
  <section class="card card--front" aria-label="Card front">
    <div class="brand"><span class="brand__mark"></span>Ben Colvin Law</div>
    <div class="holder">
      <h1 class="holder__name">Benedict R. Colvin</h1>
      <p class="holder__title">Attorney at Law</p>
    </div>
    <div class="divider"></div>
    <ul class="contact">
      <li><span class="contact__label">Tel:</span> (510) 555-0182</li>
      <li><span class="contact__label">Fax:</span> (510) 555-0193</li>
      <li><span class="contact__label">Email:</span> bencolvinlaw@quillpost.com</li>
      <li><span class="contact__label">Web:</span> www.bencolvinlaw-office.com</li>
    </ul>
    <div class="band"></div>
  </section>

  <section class="card card--back" aria-label="Card back">
    <div class="brand"><span class="brand__mark"></span>Ben Colvin Law</div>
  </section>
</main>
</body>
</html>
```